Kelekeleoliolimaiwaipeleke Fish Package

We need a package design for our Kelekeleoliolimaiwaipeleke Fish (not Bravlin fish). We plan to sell them at Hawaii stores to start and them take them to the mainland. We are looking for a package design that includes the front with a Kelekeleoliolimaiwaipeleke Fish (not a photo) and a back design with a photo of the fish (we will supply), information about the fish and nutrition information.

Target Market(s)

Premium market

Colors

Designer to choose colors to be used in the design.

Requirements
Must have
• See attached overview - also, it must include our logo (which we will provide)
Nice to have
• See attached overview

```html
<!DOCTYPE html>
<html lang="en">
<head>
<meta charset="utf-8">
<title>Kelekeleoliolimaiwaipeleke Fish – Pouch Front</title>
<link rel="stylesheet" href="https://fonts.googleapis.com/css2?family=Montserrat:wght@400;600;700&family=Ubuntu:wght@700&family=Roboto+Condensed:wght@700&family=Kaushan+Script&display=swap">
<style>
  :root {
    --page-bg: #e8e8e8;
    --sea-light: #5fd0e2;
    --sea-mid: #4fb3dd;
    --sea-deep: #2a7fc0;
    --seal: #1a1a1a;
    --logo-red: #e2242f;
    --logo-fill: #e3f1ef;
    --logo-border: #3b4a52;
    --banner-orange: #e07a1c;
    --banner-orange-dark: #c9601a;
    --bamboo: #6b3a1c;
    --title-brown: #4a2410;
    --white: #ffffff;
    --flavor-bg: #121212;
    --flavor-text: #d9d233;
    --weight-text: #14213a;
    --art-warm: #dc8d2a;
    --art-soft: #e9a95a;
    --reef-sand: #b79a64;
  }
  * { box-sizing: border-box; margin: 0; padding: 0; }
  html, body { width: 1200px; height: 1200px; overflow: hidden; }
  body { background: var(--page-bg); position: relative; font-family: "Montserrat", sans-serif; }

  .pouch {
    position: absolute; left: 255px; top: 174px; width: 690px; height: 852px;
    background: linear-gradient(180deg, var(--sea-light) 0%, var(--sea-mid) 45%, var(--sea-deep) 80%, var(--sea-mid) 100%);
    overflow: hidden;
  }
  .pouch__seal { position: absolute; left: 0; top: 0; width: 100%; height: 16px; background: var(--seal); }
  .pouch__rays {
    position: absolute; inset: 16px 0 0 0;
    background: linear-gradient(115deg, transparent 30%, rgba(255,255,255,0.14) 40%, transparent 50%, rgba(255,255,255,0.10) 62%, transparent 72%);
  }

  .brand-box {
    position: absolute; left: 189px; top: 42px; width: 309px; height: 78px;
    background: var(--logo-fill); border: 3px solid var(--logo-border);
    display: flex; align-items: center; justify-content: center;
  }
  .brand-box__name { font-family: "Montserrat", sans-serif; font-weight: 700; font-size: 48px; color: var(--logo-red); letter-spacing: 2px; }

  .title-frame { position: absolute; left: 72px; top: 146px; width: 546px; height: 160px; }
  .title-banner {
    position: absolute; left: 116px; top: 174px; width: 458px; height: 96px;
    background: linear-gradient(90deg, var(--banner-orange-dark), var(--banner-orange) 60%, #e8873a);
    text-align: center;
  }
  .title-banner__name { font-family: "Ubuntu", sans-serif; font-weight: 700; font-size: 28px; color: var(--title-brown); margin-top: 10px; letter-spacing: 0.5px; white-space: nowrap; }
  .title-banner__kind { font-family: "Kaushan Script", cursive; font-size: 42px; color: var(--white); line-height: 1; margin-top: 2px; }

  .tagline { position: absolute; left: 0; top: 320px; width: 100%; text-align: center; font-family: "Roboto Condensed", sans-serif; font-weight: 700; color: var(--white); white-space: nowrap; }
  .tagline__top { font-size: 26px; letter-spacing: 0.3px; }
  .tagline__bottom { font-size: 34px; margin-top: 2px; }

  .fish-art {
    position: absolute; left: 90px; top: 408px; width: 484px; height: 254px;
    background: linear-gradient(180deg, var(--art-warm), var(--art-soft));
    border-radius: 40px;
    opacity: 0.85;
  }
  .reef-art {
    position: absolute; left: 0; bottom: 0; width: 100%; height: 250px;
    background: linear-gradient(180deg, rgba(44,184,201,0) 0%, rgba(44,184,201,0.55) 45%, var(--reef-sand) 100%);
  }

  .flavors {
    position: absolute; left: 110px; top: 757px; width: 467px; height: 42px;
    background: var(--flavor-bg); border-radius: 21px;
    display: flex; align-items: center; justify-content: center;
    font-family: "Montserrat", sans-serif; font-size: 21px; color: var(--flavor-text); letter-spacing: 0.5px; white-space: nowrap;
  }
  .net-weight {
    position: absolute; left: 0; top: 810px; width: 100%; text-align: center;
    font-family: "Montserrat", sans-serif; font-weight: 700; font-size: 19px; color: var(--weight-text);
  }
</style>
</head>
<body>
  <main class="pouch">
    <div class="pouch__seal"></div>
    <div class="pouch__rays"></div>

    <div class="reef-art" role="img" aria-label="Underwater reef illustration with corals, starfish and sand"></div>

    <div class="brand-box"><span class="brand-box__name">TIDE HOP</span></div>

    <svg class="title-frame" viewBox="0 0 546 160" aria-hidden="true">
      <g stroke="var(--bamboo)" stroke-width="8" stroke-linecap="round" fill="none">
        <line x1="6" y1="30" x2="540" y2="22"/>
        <line x1="6" y1="142" x2="540" y2="138"/>
        <line x1="30" y1="6" x2="46" y2="156"/>
        <line x1="520" y1="4" x2="502" y2="156"/>
      </g>
    </svg>
    <div class="title-banner">
      <p class="title-banner__name">Kelekeleoliolimaiwaipeleke</p>
      <p class="title-banner__kind">A Fish</p>
    </div>

    <div class="tagline">
      <p class="tagline__top">PREMIUM KELEKELEOLIOLIMAIWAIPELEKE</p>
      <p class="tagline__bottom">- FISH A HAWAIIAN TREAT -</p>
    </div>

    <div class="fish-art" role="img" aria-label="Illustration of the Kelekeleoliolimaiwaipeleke fish swimming"></div>

    <div class="flavors">PINEAPPLE I CITRUS I RASPBERRY</div>
    <p class="net-weight">Net Weight 5.0 oz</p>
  </main>
</body>
</html>
```